Intermodal Trucking Company Website

My client is a trucking company that takes the containers you see on the back of a ship or railroad car and delivers them in the midwestern part of the United States. Here are some of their competitors Websites and their logo to use as part of the design.

http://www.varnekhaulers.example/
https://www.plirext.example/
http://www.brontagefreight.example/
https://www.lqp-xy.example/

Industry/Entity Type

Trucking Company

Number of Pages Required

2 page

Requirements
Must have
• Website must be professional and the design needs to be suitable for a responsive Website.
Should not have
• Please do not submit designs with misspellings. Designs with misspellings will be eliminated.

```html
<!DOCTYPE html>
<html lang="en">
<head>
<meta charset="utf-8">
<title>Tandem R.R. INC — Intermodal Trucking</title>
<link rel="stylesheet" href="https://fonts.googleapis.com/css2?family=Oswald:wght@400;500&family=Poppins:wght@400;500;600;700&display=swap">
<style>
:root{
  --yellow:#f6f33a;
  --orange:#d94a2b;
  --charcoal:#3f3f3f;
  --charcoal-dark:#2e2e2e;
  --text:#333333;
  --muted:#7a7a7a;
  --panel:#e9e9e9;
  --line:#d3d3d3;
  --white:#ffffff;
}
*{box-sizing:border-box;margin:0;padding:0}
html,body{width:1200px;height:2356px;overflow:hidden}
body{position:relative;background:var(--white);font-family:"Poppins",sans-serif;color:var(--text)}
.abs{position:absolute}
.heading{font-family:"Oswald",sans-serif;font-weight:500;text-transform:uppercase;color:#222;font-size:21px;letter-spacing:.2px}

/* header */
.site-header{left:0;top:0;width:1200px;height:132px;background:linear-gradient(#cfcfcf,#bdbdbd)}
.brand{left:0;top:0;width:370px;height:160px;background:var(--charcoal);clip-path:polygon(0 0,310px 0,370px 160px,0 160px);display:flex;align-items:center;padding-left:40px}
.brand-stripe{left:296px;top:0;width:80px;height:160px;background:var(--orange);clip-path:polygon(6px 0,18px 0,80px 160px,68px 160px)}
.brand-name{font-family:"Poppins",sans-serif;font-weight:700;font-size:27px;color:var(--yellow);display:flex;align-items:center;gap:12px}
.brand-name i{display:block;width:16px;height:16px;background:var(--yellow)}
.contact-top{left:536px;top:35px;font-size:18px;font-weight:500;color:#333;display:flex;gap:18px;align-items:center}
.contact-top b{font-weight:600}
.social{display:flex;gap:5px;margin-left:6px}
.social span{width:24px;height:24px;border:2px solid #444;border-radius:50%}
.search{left:935px;top:31px;width:196px;height:35px;background:#ececec;border:1px solid #b5b5b5;font-size:14px;color:#888;padding:7px 10px}
.search svg{position:absolute;right:10px;top:8px}
.main-nav{left:358px;top:94px;width:842px;height:36px;background:var(--yellow);clip-path:polygon(0 0,100% 0,100% 100%,14px 100%)}
.main-nav a{position:absolute;top:6px;font-family:"Oswald",sans-serif;font-size:19px;color:#222;text-decoration:none;text-transform:uppercase;white-space:nowrap}

/* hero */
.hero{left:0;top:132px;width:1200px;height:547px;background:linear-gradient(100deg,#3a4a6a 0%,#1f2b45 35%,#4b6fa0 60%,#8fb6d8 85%,#bfd7ea 100%)}
.hero-panel{left:679px;top:267px;width:447px;height:233px;background:rgba(40,55,80,.72);padding:18px 22px}
.hero-panel h1{font-family:"Poppins",sans-serif;font-weight:600;font-size:31px;line-height:40px;color:var(--white);white-space:nowrap;letter-spacing:-.3px}
.hero-panel h1 span{font-size:25px}
.hero-panel p{font-size:21px;color:var(--white);margin-top:12px;white-space:nowrap}
.btn-yellow{display:inline-block;background:var(--yellow);color:#111;font-weight:700;font-size:17px;padding:6px 13px;text-transform:uppercase}
.hero-panel .btn-yellow{position:absolute;left:23px;top:170px}

/* about */
.about{left:74px;top:722px;width:660px}
.about p{font-size:14px;line-height:26px;color:var(--muted);margin-top:14px}
.divider-v{left:774px;top:722px;width:1px;height:246px;background:var(--line)}
.services{left:793px;top:722px;width:340px}
.services ul{list-style:none;margin-top:14px}
.services li{font-size:14px;color:var(--muted);line-height:35px;padding-left:18px;position:relative}
.services li::before{content:"";position:absolute;left:2px;top:14px;border-left:5px solid #999;border-top:4px solid transparent;border-bottom:4px solid transparent}

/* service band */
.band{left:0;top:1013px;width:1200px;height:327px;background:linear-gradient(180deg,#6a5a5c 0%,#b56e55 45%,#5b4440 75%,#3a3534 100%)}
.service-card{top:1148px;width:242px;height:109px;background:var(--white);text-align:center;font-weight:600;font-size:19px;line-height:22px;color:#222;padding-top:40px}
.service-icon{top:1104px;width:76px;height:76px;border-radius:50%;background:var(--white);display:flex;align-items:center;justify-content:center}

/* widgets */
.widget{top:1390px;height:240px;background:var(--panel);border:1px solid var(--line);padding:14px 18px}
.widget .heading{border-bottom:3px solid var(--line);padding-bottom:6px}
.field{position:absolute;height:39px;background:var(--white);border:1px solid #d8d8d8;font-size:15px;color:#888;padding:9px 11px}
.field svg{position:absolute;right:10px;top:15px}
.btn-orange{position:absolute;background:var(--orange);color:var(--white);font-weight:700;font-size:21px;text-transform:uppercase;text-align:center;line-height:38px}
.testimonial{left:427px;top:1392px;width:347px;text-align:center}
.testimonial p{font-size:14px;line-height:24px;color:var(--muted);margin-top:14px;padding:0 22px;position:relative}
.testimonial .q{position:absolute;font-family:Georgia,serif;font-size:46px;color:#bbb;line-height:1}
.testimonial cite{display:block;font-style:normal;font-weight:700;font-size:14px;color:#444;margin-top:6px}
.testimonial small{display:block;font-size:13px;color:#666}
.dots{display:flex;justify-content:center;gap:4px;margin-top:10px}
.dots span{width:9px;height:9px;border-radius:50%;background:#d0d0d0}
.dots span:first-child{background:#666}

/* promos */
.promo{top:1687px;width:512px;height:287px;padding:28px 36px}
.promo h2{font-family:"Oswald",sans-serif;font-weight:500;font-size:38px;line-height:36px;color:var(--white);text-transform:uppercase;letter-spacing:-.5px}
.promo p{font-size:14px;line-height:24px;color:var(--white);margin-top:10px}
.promo .btn-yellow{font-size:12px;padding:4px 9px;margin-top:18px}

/* footer */
.footer{left:0;top:2033px;width:1200px;height:279px;background:var(--charcoal);border-top:4px solid var(--yellow)}
.footer-title{font-size:16px;font-weight:600;color:var(--white)}
.quick-links ul{list-style:none;margin-top:16px}
.quick-links li{font-size:14px;color:#ddd;line-height:32.5px;padding-left:14px;position:relative}
.quick-links li::before{content:"";position:absolute;left:0;top:12px;border-left:5px solid #aaa;border-top:4px solid transparent;border-bottom:4px solid transparent}
.map{left:344px;top:2113px;width:242px;height:158px;background:linear-gradient(135deg,#eae6dc,#dcdcd2 60%,#cfd8e0);border:1px solid #999}
.address{left:605px;top:2110px;width:145px;font-size:14px;line-height:24px;color:#eee;white-space:nowrap}
.address .social span{border-color:#eee;width:22px;height:22px}
.footer .field{height:37px;border-color:#ccc}
.copyright{left:0;top:2312px;width:1200px;height:44px;background:var(--charcoal-dark);color:#ddd;font-size:14px;text-align:center;line-height:44px}
</style>
</head>
<body>

<header>
  <div class="abs site-header"></div>
  <div class="abs brand"><span class="brand-name"><i></i>Tandem R.R. INC</span></div>
  <div class="abs brand-stripe"></div>
  <div class="abs contact-top">
    <span>Larkfield, KS</span><b>555-014-2290</b>
    <span class="social"><span></span><span></span><span></span></span>
  </div>
  <div class="abs search">Search
    <svg width="18" height="18" viewBox="0 0 18 18" fill="none" stroke="#333" stroke-width="2"><circle cx="7.5" cy="7.5" r="5.5"/><path d="M11.5 11.5l5 5"/></svg>
  </div>
  <nav class="abs main-nav">
    <a style="left:193px">Home</a>
    <a style="left:287px">About</a>
    <a style="left:387px">News and Events</a>
    <a style="left:572px">Services</a>
    <a style="left:693px">Contact</a>
  </nav>
</header>

<section>
  <div class="abs hero" role="img" aria-label="Photo of a blue semi truck hauling a shipping container at a port container yard"></div>
  <div class="abs hero-panel">
    <h1>Lorem Ipsum Dolor Sit<br><span>Consectetur Adipiscing Elit</span></h1>
    <p>Sed do eiusmod tempor incididunt</p>
    <a class="btn-yellow">Learn More</a>
  </div>
</section>

<section>
  <div class="abs about">
    <h2 class="heading">About Tandem R.R. INC</h2>
    <p>Lorem ipsum dolor sit amet, consectetur adipiscing elit, sed do eiusmod tempor incididunt ut labore et dolore magna aliqua. Ut enim ad minim veniam, quis nostrud exercitation ullamco laboris nisi ut aliquip ex ea commodo consequat. Duis aute irure dolor in reprehenderit in voluptate velit esse cillum dolore eu fugiat nulla pariatur. Excepteur sint occaecat cupidatat non proident, sunt in culpa qui officia deserunt mollit anim id est laborum.</p>
    <p>Duis aute irure dolor in reprehenderit in voluptate velit esse cillum dolore eu fugiat nulla pariatur. Excepteur sint occaecat cupidatat non proident, sunt in culpa qui officia.</p>
  </div>
  <div class="abs divider-v"></div>
  <div class="abs services">
    <h2 class="heading">Comprehensive Services</h2>
    <ul>
      <li>Drayage, Heavy Haul</li>
      <li>Hazmat, Liquids, ISO Tank</li>
      <li>Warehousing, Cross-Dock, Block &amp; Brace</li>
      <li>Short/Long Term Storage</li>
      <li>Transload, Break Bulk, Consolidation Loads</li>
      <li>Truckload Brokerage</li>
    </ul>
  </div>
</section>

<section>
  <div class="abs band" role="img" aria-label="Photo of a red semi truck with trailer on a highway at sunset"></div>
  <div class="abs service-icon" style="left:301px">
    <svg width="40" height="28" viewBox="0 0 40 28" fill="none" stroke="#d94a2b" stroke-width="2.5"><rect x="2" y="3" width="36" height="22"/><path d="M10 3v22M16 3v22M22 3v22M28 3v22M34 3v22"/></svg>
  </div>
  <div class="abs service-card" style="left:218px">Trucking Shipping<br>Services</div>
  <div class="abs service-icon" style="left:562px">
    <svg width="44" height="28" viewBox="0 0 44 28" fill="none" stroke="#d94a2b" stroke-width="2.5"><rect x="2" y="3" width="28" height="16"/><path d="M30 8h7l5 6v5H30z"/><circle cx="10" cy="23" r="3"/><circle cx="34" cy="23" r="3"/></svg>
  </div>
  <div class="abs service-card" style="left:479px">Specialty Freight &amp;<br>Shipping Services</div>
  <div class="abs service-icon" style="left:823px">
    <svg width="40" height="40" viewBox="0 0 40 40" fill="none" stroke="#d94a2b" stroke-width="3"><circle cx="15" cy="24" r="8"/><circle cx="15" cy="24" r="3"/><circle cx="29" cy="11" r="6"/><circle cx="29" cy="11" r="2"/></svg>
  </div>
  <div class="abs service-card" style="left:740px">Logistics<br>Management</div>
</section>

<section>
  <div class="abs widget" style="left:74px;width:331px">
    <h2 class="heading">Tracking</h2>
  </div>
  <div class="abs field" style="left:93px;top:1466px;width:293px">Reference or Bill of Lading</div>
  <div class="abs field" style="left:93px;top:1514px;width:293px">Container</div>
  <div class="btn-orange" style="left:93px;top:1574px;width:138px">Track It</div>

  <div class="abs testimonial">
    <h2 class="heading">Testimonials</h2>
    <p><span class="q" style="left:4px;top:-4px">&ldquo;</span>Lorem ipsum dolor sit amet, consectetur adipiscing elit, sed do eiusmod tempor incididunt ut labore et dolore magna aliqua. Ut enim ad minim veniam, quis nostrud exercitation ullamco laboris nisi ut.<span class="q" style="right:6px;bottom:-22px">&rdquo;</span></p>
    <cite>Milo Brandt</cite>
    <small>Lorem ipsum dolor</small>
    <div class="dots"><span></span><span></span><span></span></div>
  </div>

  <div class="abs widget" style="left:793px;width:333px">
    <h2 class="heading">Get a Quote</h2>
  </div>
  <div class="abs field" style="left:812px;top:1466px;width:188px">City</div>
  <div class="abs field" style="left:1010px;top:1466px;width:97px">State<svg width="14" height="8" viewBox="0 0 14 8"><path d="M0 0h14L7 8z" fill="#555"/></svg></div>
  <div class="abs field" style="left:812px;top:1514px;width:188px">City</div>
  <div class="abs field" style="left:1010px;top:1514px;width:97px">State<svg width="14" height="8" viewBox="0 0 14 8"><path d="M0 0h14L7 8z" fill="#555"/></svg></div>
  <div class="btn-orange" style="left:812px;top:1574px;width:139px">Submit</div>
</section>

<section>
  <div class="abs promo" style="left:74px;background:linear-gradient(120deg,#3d4650,#5a5a52 55%,#6e6440)" role="img" aria-label="Photo of a container handler loading a truck at a freight yard">
    <h2>Making<br>Transportation<br>Fast and Safe</h2>
    <p>orem ipsum dolor sit amet, consectetur adipiscing elit,<br>sed do eiusmod tempor incididunt ut labore.</p>
    <a class="btn-yellow">Learn More</a>
  </div>
  <div class="abs promo" style="left:614px;background:linear-gradient(120deg,#3a3f44,#565c62 55%,#7d8388)" role="img" aria-label="Photo of a truck driver standing by the cab door of his truck">
    <h2>Become<br>a Tandem R. R.<br>Truck Driver</h2>
    <p>orem ipsum dolor sit amet, consectetur adipiscing elit,<br>sed do eiusmod tempor incididunt ut labore.</p>
    <a class="btn-yellow">Learn More</a>
  </div>
</section>

<footer>
  <div class="abs footer"></div>
  <div class="abs quick-links" style="left:74px;top:2070px">
    <h3 class="footer-title">Quick Links</h3>
    <ul><li>Home</li><li>About</li><li>News and Events</li><li>Services</li><li>Contact</li></ul>
  </div>
  <h3 class="abs footer-title" style="left:344px;top:2070px">Contact Address</h3>
  <div class="abs map" role="img" aria-label="Street map of the company location"></div>
  <div class="abs address">
    Larkfield, KS<br>555-014-2290<br>info@tdrr.example
    <div class="social" style="margin:6px 0 0 0"><span></span><span></span><span></span></div>
  </div>
  <div class="abs field" style="left:757px;top:2110px;width:179px">Name</div>
  <div class="abs field" style="left:946px;top:2110px;width:179px">Email</div>
  <div class="abs field" style="left:757px;top:2157px;width:368px;height:67px">Message</div>
  <div class="btn-orange" style="left:757px;top:2235px;width:212px">Send Message</div>
  <div class="abs copyright">Copyright © 2017 Tandem R.R. INC &nbsp;|&nbsp; Terms &nbsp;|&nbsp; All Rights Reserved</div>
</footer>

</body>
</html>
```